Vehicle Graphics for Brookfield Key Mobile Locksmith

We're seeking vehicle graphics for a locksmith business in Colorado called Brookfield Key. Our service area is located in the Rocky Mountains near several world-class ski resorts, which fuel the local economy. We are a comprehensive locksmith business offering automotive, commercial and residential services. We provide modern, tech-savvy digital security solutions for your home or business. The final design should be a compliment to our existing website, logo and ad creative.

The work vehicle is a 2020 Varlen Korvo, color is Pewter Haze Metallic. The truck has a topper, color is Ashen Tone. The vehicle graphics will be for the topper only. The truck is a leased vehicle, so we will not need graphics for the truck.

Truck Topper Size
Sides = 64" wide x 26" tall
Back Panel = 60" wide x 46" tall

Target Market(s)

Local residents, businesses, hotels and resorts. As well as visitors to the ski areas that may need emergency lock out services. High income, high net worth clients. Also, lots of customers that have lost their car keys.

Industry/Entity Type

Locksmith

Font styles to use
Sans Serif

Requirements
Must have
• *Include: Logo
*Include: 555.218.3967
*Include: brookfieldkey.example
*Include text: Auto | Residential | Commercial
*Include: Dependable Entry Service
*Colors from the logo are the main colors to use; accent color is Chrome Yellow (#ffac00)
*Bank Gothic is the headline font and we like to use Oswald font for all other text
*Colors/design must compliment truck and truck topper colors (listed above).
Nice to have
• We'd like the design to be clean, professional, and easy to see/read. Nothing complicated. Nothing cluttered. Back panel design of the topper should look different from the (2) side panels.

The design does NOT need to mirror the print advertisement.
Should not have
• Please do not include Raj's (the locksmith) photo from the print advertisement.

```html
<!DOCTYPE html>
<html lang="en">
<head>
<meta charset="utf-8">
<title>Brookfield Key – Topper Graphics</title>
<link rel="stylesheet" href="https://fonts.googleapis.com/css2?family=Michroma&family=Oswald:wght@400;500&display=swap">
<style>
  :root {
    --brand-blue: #1f7ac2;
    --deep-blue: #1b4a6e;
    --chrome-yellow: #ffac00;
    --topper-grey: #a3a29e;
    --stripe-grey: #8a8985;
    --paper: #ffffff;
  }
  html, body {
    margin: 0;
    width: 848px;
    height: 1200px;
    overflow: hidden;
    background: var(--paper);
  }
  .sheet {
    position: relative;
    width: 848px;
    height: 1200px;
  }
  .panel {
    position: absolute;
    display: block;
  }
  .panel--side { left: 104px; top: 200px; width: 640px; height: 260px; }
  .panel--back { left: 184px; top: 680px; width: 480px; height: 368px; }
  .view-label {
    position: absolute;
    left: 0;
    width: 848px;
    margin: 0;
    text-align: center;
    font-family: "Oswald", sans-serif;
    font-weight: 500;
    font-size: 80px;
    line-height: 1;
    letter-spacing: 6px;
    color: var(--deep-blue);
  }
  .view-label--side { top: 500px; }
  .view-label--back { top: 1090px; }
  .topper-bg { fill: var(--topper-grey); }
  .band-blue { fill: var(--brand-blue); }
  .band-yellow { fill: var(--chrome-yellow); }
  .band-grey { fill: var(--stripe-grey); }
  .phone {
    font-family: "Oswald", sans-serif;
    font-weight: 500;
    fill: var(--chrome-yellow);
  }
  .headline {
    font-family: "Michroma", sans-serif;
    fill: var(--brand-blue);
  }
  .brand-name {
    font-family: "Oswald", sans-serif;
    font-weight: 500;
    fill: var(--brand-blue);
  }
  .brand-dot { fill: var(--brand-blue); }
  .web-address {
    font-family: "Oswald", sans-serif;
    font-weight: 400;
    fill: var(--deep-blue);
  }
  .service {
    font-family: "Oswald", sans-serif;
    font-weight: 400;
    fill: var(--brand-blue);
  }
  .icon { fill: var(--brand-blue); }
  .icon-cutout { fill: var(--topper-grey); }
</style>
</head>
<body>
<main class="sheet">

  <svg width="0" height="0" style="position:absolute" aria-hidden="true">
    <defs>
      <symbol id="icon-car" viewBox="0 0 20 20">
        <polygon class="icon" points="4,9 6.5,4 13.5,4 16,9"/>
        <rect class="icon" x="1" y="8.5" width="18" height="6.5" rx="2"/>
        <circle class="icon" cx="5" cy="16" r="2.2"/>
        <circle class="icon" cx="15" cy="16" r="2.2"/>
      </symbol>
      <symbol id="icon-house" viewBox="0 0 20 20">
        <polygon class="icon" points="10,1.5 19,9.5 16.5,9.5 16.5,18 3.5,18 3.5,9.5 1,9.5"/>
        <rect class="icon-cutout" x="8" y="12" width="4" height="6"/>
      </symbol>
      <symbol id="icon-building" viewBox="0 0 20 20">
        <rect class="icon" x="3" y="2" width="14" height="17"/>
        <rect class="icon-cutout" x="5.5" y="5" width="2.5" height="2.5"/>
        <rect class="icon-cutout" x="12" y="5" width="2.5" height="2.5"/>
        <rect class="icon-cutout" x="5.5" y="10" width="2.5" height="2.5"/>
        <rect class="icon-cutout" x="12" y="10" width="2.5" height="2.5"/>
        <rect class="icon-cutout" x="8.5" y="15" width="3" height="4"/>
      </symbol>
      <linearGradient id="keys-tone" x1="0" y1="0" x2="1" y2="1">
        <stop offset="0" stop-color="#3a3b3d"/>
        <stop offset="0.5" stop-color="#1d1e20"/>
        <stop offset="1" stop-color="#6e6f71"/>
      </linearGradient>
    </defs>
  </svg>

  <!-- Side panel -->
  <svg class="panel panel--side" viewBox="0 0 640 260" aria-label="Side topper panel">
    <rect class="topper-bg" x="0" y="0" width="640" height="260"/>
    <polygon class="band-blue" points="0,0 400,0 372,70 0,70"/>
    <polygon class="band-yellow" points="408,0 424,0 396,70 380,70"/>
    <polygon class="band-yellow" points="0,78 368,78 364,86 0,86"/>
    <polygon class="band-yellow" points="0,94 340,94 290,250 0,250"/>
    <polygon class="band-grey" points="0,224 298,224 294,234 0,234"/>
    <polygon role="img" aria-label="Close-up photo of assorted car key fobs" fill="url(#keys-tone)" points="336,94 470,94 442,170 312,170"/>
    <text class="phone" x="186" y="54" font-size="44" text-anchor="middle">555.218.3967</text>
    <text class="headline" x="28" y="134" font-size="23">DEPENDABLE</text>
    <text class="headline" x="28" y="170" font-size="23">ENTRY</text>
    <text class="headline" x="28" y="206" font-size="23">SERVICE</text>

    <circle class="brand-dot" cx="445" cy="44" r="15"/>
    <text class="brand-name" x="468" y="55" font-size="28">Brookfield Key</text>
    <polygon class="band-yellow" points="432,94 640,94 640,122 422,122"/>
    <text class="web-address" x="532" y="115" font-size="17" text-anchor="middle">brookfieldkey.example</text>

    <use href="#icon-car" x="464" y="138" width="20" height="20"/>
    <text class="service" x="490" y="155" font-size="20">Auto</text>
    <use href="#icon-house" x="464" y="170" width="20" height="20"/>
    <text class="service" x="490" y="187" font-size="20">Residential</text>
    <use href="#icon-building" x="464" y="202" width="20" height="20"/>
    <text class="service" x="490" y="219" font-size="20">Commercial</text>
  </svg>
  <h2 class="view-label view-label--side">SIDE</h2>

  <!-- Back panel -->
  <svg class="panel panel--back" viewBox="0 0 600 460" aria-label="Back topper panel">
    <rect class="topper-bg" x="0" y="0" width="600" height="460"/>
    <polygon class="band-blue" points="0,0 562,0 536,36 0,36"/>
    <text class="phone" x="290" y="29" font-size="30" text-anchor="middle">555.218.3967</text>
    <polygon role="img" aria-label="Close-up photo of black car key fobs" fill="url(#keys-tone)" points="0,46 256,46 256,260 202,460 0,460"/>

    <circle class="brand-dot" cx="298" cy="186" r="26"/>
    <text class="brand-name" x="336" y="200" font-size="40">Brookfield Key</text>
    <polygon class="band-yellow" points="252,250 568,250 568,290 242,290"/>
    <text class="web-address" x="405" y="280" font-size="26" text-anchor="middle">brookfieldkey.example</text>

    <use href="#icon-car" x="308" y="306" width="30" height="30"/>
    <text class="service" x="346" y="332" font-size="30">Auto</text>
    <use href="#icon-house" x="308" y="348" width="30" height="30"/>
    <text class="service" x="346" y="374" font-size="30">Residential</text>
    <use href="#icon-building" x="308" y="390" width="30" height="30"/>
    <text class="service" x="346" y="416" font-size="30">Commercial</text>
  </svg>
  <h2 class="view-label view-label--back">BACK</h2>

</main>
</body>
</html>
```